Business Card Design Project

Business card for law firm
Use existing logo
Must have:
Gordon P. Haskell
3721-C West 14th
McAllen, TX 78599
ghaskell@bvlawgroup.example
www.bvlawgroup.example
956-555-0143

Target Market(s)

Clients and potential clients, generally adult, business background

Industry/Entity Type

Business

Requirements
Must have
• Our logo, see below

```html
<!DOCTYPE html>
<html lang="en">
<head>
<meta charset="utf-8">
<title>Briarwood Vance – Business Card</title>
<link rel="stylesheet" href="https://fonts.googleapis.com/css2?family=Cinzel:wght@400;700&display=swap">
<style>
  :root {
    --page: #fdfdfd;
    --card-shadow: #e2e2e3;
    --panel-light: #bdbec0;
    --band-white: #ffffff;
    --panel-mid: #707070;
    --panel-dark: #2a2a2a;
    --firm-ink: #3a3c41;
    --contact-ink: #f2f2f2;
  }
  html, body {
    margin: 0;
    padding: 0;
    width: 1200px;
    height: 1000px;
    overflow: hidden;
    background: var(--page);
  }
  .business-card {
    display: block;
    width: 1200px;
    height: 1000px;
  }
  .firm-name {
    font-family: "Cinzel", serif;
    font-weight: 400;
    font-size: 22px;
    fill: var(--firm-ink);
    letter-spacing: 0.3px;
  }
  .firm-square { fill: var(--firm-ink); }
  .contact-line {
    font-family: "Cinzel", serif;
    font-weight: 400;
    font-size: 12.5px;
    fill: var(--contact-ink);
    letter-spacing: 0.3px;
  }
  .contact-name {
    font-weight: 700;
    font-size: 13.5px;
  }
</style>
</head>
<body>
<svg class="business-card" viewBox="0 0 1200 1000" xmlns="http://www.w3.org/2000/svg" aria-label="Briarwood Vance business card for Gordon P. Haskell">
  <rect class="card-shadow" x="369" y="368" width="497" height="293" fill="var(--card-shadow)"/>

  <g class="card-face">
    <rect class="panel-light" x="358" y="358" width="497" height="293" fill="var(--panel-light)"/>
    <polygon class="band-white" points="680,358 855,358 855,651 395,651" fill="var(--band-white)"/>
    <polygon class="panel-dark" points="745,358 855,358 855,651 805,651 632,478" fill="var(--panel-dark)"/>
    <polygon class="panel-mid" points="595,515 731,651 458,651" fill="var(--panel-mid)"/>
  </g>

  <g class="firm-mark" transform="translate(432,606) rotate(-45)">
    <rect class="firm-square" x="-20" y="-17" width="16" height="16"/>
    <text class="firm-name" x="4" y="0">Briarwood Vance</text>
  </g>

  <g class="contact-block" transform="translate(713,413) rotate(45)">
    <text class="contact-line contact-name" x="0" y="0">Gordon P. Haskell</text>
    <text class="contact-line" x="0" y="16">3721-C West 14th</text>
    <text class="contact-line" x="0" y="32">McAllen, TX 78599</text>
    <text class="contact-line" x="0" y="48">ghaskell@bvlawgroup.example</text>
    <text class="contact-line" x="0" y="64">www.bvlawgroup.example</text>
    <text class="contact-line" x="0" y="80">956-555-0143</text>
  </g>
</svg>
</body>
</html>
```